KORU product web page

We need a new web design for our KORU product page. You can find more information about the project on the current web site - www.koru-example.io

What we need from a new design (uncoded):
- landing pages + template
- all information on one page
- the design should be focused on the product - light bulb + app
- web site should be with some dynamics like a background with parallax effect in the current version
- fonts should be chosen
- a number of illustrations should be designed

Here is schema for a new design: https://files.example-share.net/drawings/d/7Qm2Lr9Xk4Pz8Wn3Ty6Vb1Hc5Jd0Fg2Ks4Na/edit

Here is a document with all texts for a new design: https://files.example-share.net/document/d/3Zt8Mp1Rw6Yc9Lk2Hs5Gv0Bn4Xq7Df3Ju8Pe/edit

Illustrations to use:
v1 - https://files.example-share.net/folder?id=4Kp7Tr2Wn9Qs5Lm1Zx8Cv3Bd&share=1
v2 - https://files.example-share.net/folder?id=4Kp7Tr2Wn9Qs6Hy3Rf0Gj5Mk&share=1

uOS screens: https://files.example-share.net/folder?id=9Vd2Ls6Nq1Xw8Pt4Jh7Ec3Ra&share=1

KORU logo: https://files.example-share.net/folder?id=4Kp7Tr2Wn9Qs2Yb6Uc8Fz0Ow&share=1
Updates

I forgot to add the definition text "KORU - is.." to the document with texts. Sorry, my mistake.

Target Market(s)

25-45 year old adults who are interested in "smart" devices for their health.

Industry/Entity Type

Google

Colors

Designer to choose colors to be used in the design.

Requirements
Must have
• - landing pages + template
- fonts should be chosen

```html
<!DOCTYPE html>
<html lang="en">
<head>
<meta charset="utf-8">
<title>KORU — Smart Lightbulb</title>
<link href="https://fonts.googleapis.com/css2?family=Open+Sans:wght@400;600;700&display=swap" rel="stylesheet">
<style>
:root{
  --green:#4f9d2f;
  --green-bright:#5cb336;
  --green-deep:#46922a;
  --dark:#3a3a3a;
  --darker:#2b2b2b;
  --blue:#72b4da;
  --white:#ffffff;
  --text:#4a4a4a;
}
*{margin:0;padding:0;box-sizing:border-box}
html,body{width:1200px;height:2951px;overflow:hidden}
body{font-family:"Open Sans",Arial,sans-serif;color:var(--text);background:var(--white);position:relative}
section,header,footer{position:absolute;left:0;width:1200px}
.abs{position:absolute}

/* header */
.site-header{top:0;height:134px;background:var(--white)}
.brand{left:116px;top:0;width:128px;height:126px;border-radius:50%;background:var(--green-bright);display:flex;align-items:center;justify-content:center;color:var(--white);font-weight:700;font-size:30px;letter-spacing:1px}
.main-nav{right:82px;top:56px;display:flex;gap:30px;font-size:14px;font-weight:600;color:#333;text-transform:uppercase}
.main-nav .active{color:var(--green)}

/* hero */
.hero{top:134px;height:515px;background:radial-gradient(ellipse at 35% 40%,#6c6a5a 0%,#3c3a30 40%,#22231c 70%),linear-gradient(90deg,#2a2a22,#3f7a2a)}
.hero-photo{left:0;top:0;width:1200px;height:515px;background:radial-gradient(ellipse at 30% 45%,rgba(220,210,170,.55),rgba(0,0,0,0) 35%),radial-gradient(ellipse at 60% 35%,rgba(140,190,90,.55),rgba(0,0,0,0) 30%),linear-gradient(90deg,rgba(30,30,25,.2) 0%,rgba(30,30,25,0) 50%,rgba(60,140,40,.85) 100%)}
.hero-title{left:704px;top:200px;font-size:35px;font-weight:700;color:var(--white);text-transform:uppercase}
.hero-sub{left:704px;top:268px;width:400px;font-size:17px;font-weight:600;line-height:26px;color:var(--white)}
.btn{height:47px;width:144px;display:flex;align-items:center;justify-content:center;font-size:15px;font-weight:700;color:var(--white);text-transform:uppercase;border-radius:3px}
.btn-dark{left:708px;top:350px;background:#2e2e2e}
.btn-green{left:889px;top:350px;background:var(--green-bright)}
.slide-arrow{top:228px;width:47px;height:47px;border:1px solid rgba(255,255,255,.35);background:rgba(0,0,0,.35);display:flex;align-items:center;justify-content:center}
.slide-arrow.prev{left:12px}
.slide-arrow.next{left:1130px}

/* intro */
.intro{top:649px;height:236px;background:var(--white)}
.intro p{position:absolute;left:118px;top:28px;width:968px;font-size:13.5px;line-height:23px;text-align:center;color:#555}

.scroll-cue{width:50px;height:50px;border-radius:50%;background:#f1f1f1;border:2px solid #cfcfcf;left:575px;display:flex;align-items:center;justify-content:center;z-index:5}

/* feature panels */
.feature{top:0;height:100%;width:600px;color:var(--white)}
.feature h2{position:absolute;left:47px;top:26px;font-size:38px;font-weight:600}
.feature p{font-size:13.5px;line-height:24px}
.row-one{top:885px;height:547px}
.row-two{top:1432px;height:545px}
.panel-green{left:0;background:var(--green)}
.panel-dark{left:600px;background:var(--dark)}
.panel-darker{left:0;background:var(--darker)}
.panel-blue{left:600px;background:var(--blue)}
.phone-shot{left:47px;top:93px;width:165px;height:364px;border-radius:26px;background:linear-gradient(180deg,#2c2c2c 0%,#e9ece6 18%,#dfe4dc 80%,#2c2c2c 100%)}
.app-copy{left:236px;top:118px;width:320px}
.app-copy p{margin-bottom:24px}
.color-shot{left:49px;top:95px;width:496px;height:218px;background:radial-gradient(ellipse at 30% 20%,#5fe04a 0%,#2a7a20 30%,#0f2a0c 70%),#111}
.color-copy{left:49px;top:345px;width:500px}
.health-icon{left:206px;top:108px;width:174px;height:142px;border-radius:40% 40% 50% 50%;background:linear-gradient(180deg,#e0302f,#b71c1c)}
.health-copy{left:22px;top:300px;width:560px}
.health-copy p{margin-bottom:24px}
.lamp-icon{left:248px;top:108px;width:100px;height:110px;border-radius:50% 50% 8px 8px;background:var(--white);opacity:.92}
.lamp-copy{left:28px;top:278px;width:552px}
.lamp-copy p{margin-bottom:24px}

/* specs */
.specs{top:1977px;height:478px;background:var(--green-deep);color:var(--white)}
.specs h2{position:absolute;left:0;width:1200px;top:30px;text-align:center;font-size:40px;font-weight:600;line-height:52px}
.tools-icon{left:552px;top:104px;width:112px;height:108px;border-radius:10px;background:#1f1f1f}
.spec-copy{left:118px;top:250px;width:620px;font-size:13.5px;line-height:22px}
.spec-copy p{margin-bottom:22px}
.compat{left:767px;top:248px;width:360px}
.compat h3{font-size:19px;font-weight:600;margin-bottom:18px}
.compat li{list-style:none;font-size:13.5px;margin-bottom:22px;padding-left:26px;position:relative}
.compat li::before{content:"";position:absolute;left:4px;top:7px;width:7px;height:7px;border-radius:50%;background:var(--white)}

/* signup */
.signup{top:2455px;height:283px;background:radial-gradient(ellipse at 85% 40%,#6b6b63 0%,#3a3833 30%,#1f1e1b 70%)}
.signup-photo{left:0;top:0;width:1200px;height:283px;background:linear-gradient(90deg,rgba(0,0,0,.2),rgba(0,0,0,0) 60%)}
.signup h2{position:absolute;left:0;width:1200px;top:44px;text-align:center;font-size:34px;font-weight:600;color:var(--white)}
.signup p{position:absolute;left:340px;width:520px;top:112px;text-align:center;font-size:13.5px;line-height:26px;color:#ddd}
.email-field{left:401px;top:200px;width:466px;height:50px;background:var(--white);border-radius:5px;display:flex;align-items:center;padding-left:16px;font-size:13px;color:#888;gap:12px}
.email-go{position:absolute;right:6px;top:5px;width:40px;height:40px;border-radius:50%;background:#eee;border:2px solid #ccc;display:flex;align-items:center;justify-content:center}

/* footer */
.site-footer{top:2738px;height:213px;background:var(--dark);color:#ddd}
.footer-col h4{font-size:17px;font-weight:400;text-transform:uppercase;color:#eee;margin-bottom:20px}
.contact-col{left:112px;top:34px;width:300px}
.contact-item{display:flex;gap:14px;font-size:13px;line-height:20px;margin-bottom:16px;align-items:flex-start}
.contact-item.phone{font-size:18px;align-items:center}
.social-col{left:488px;top:34px;width:300px}
.social-item{display:flex;align-items:center;gap:18px;font-size:13px;margin-bottom:12px}
.social-dot{width:22px;height:22px;border-radius:50%;background:#7a7a7a}
.legal-col{left:826px;top:34px;width:290px;font-size:13px;line-height:26px;text-align:right}
.legal-col .links span{margin:0 6px}
</style>
</head>
<body>

<header class="site-header">
  <div class="abs brand">KORU</div>
  <nav class="abs main-nav">
    <span class="active">Pre order</span><span>Blog</span><span>Contact us</span><span>RU</span>
  </nav>
</header>

<section class="hero">
  <div class="abs hero-photo" role="img" aria-label="Photograph of two glowing KORU smart LED lightbulbs on a dark table with warm and green bokeh light"></div>
  <div class="abs slide-arrow prev"><svg width="14" height="20" viewBox="0 0 14 20"><path d="M11 2 3 10l8 8" fill="none" stroke="#fff" stroke-width="3"/></svg></div>
  <div class="abs slide-arrow next"><svg width="14" height="20" viewBox="0 0 14 20"><path d="M3 2l8 8-8 8" fill="none" stroke="#fff" stroke-width="3"/></svg></div>
  <h1 class="abs hero-title">Turn your KORU on!</h1>
  <p class="abs hero-sub">Create light scenes and adapt them to your needs with KORU App</p>
  <a class="abs btn btn-dark">Pre-order</a>
  <a class="abs btn btn-green">View more</a>
</section>

<section class="intro">
  <p>Ut suscipit gravida neque sit amet pulvinar. Praesent congue pharetra massa nec laoreet. Cras cursus quam libero, et rutrum purus tristique sit amet. Aenean sem erat, placerat at elementum vel, posuere dictum nulla. Maecenas tristique, dolor vitae consectetur rutrum, ante odio tincidunt sem, quis consectetur est elit nec ante. Vestibulum et mauris suscipit, ultricies mauris in, tristique tortor. Etiam id sapien sed arcu pretium condimentum vel eget massa. Nunc eget lacinia turpis, a malesuada arcu. Aliquam non erat ante. Aliquam at sodales nunc, sit amet vehicula ipsum. Duis varius magna eros, quis posuere sem eleifend a. Pellentesque vulputate, nisi in viverra blandit, neque felis sagittis quam, in ullamcorper lorem magna nec risus. Vestibulum magna sapien, pretium porta euismod a, imperdiet a dui.</p>
  <div class="abs scroll-cue" style="top:178px"><svg width="18" height="12" viewBox="0 0 18 12"><path d="M2 2l7 7 7-7" fill="none" stroke="#666" stroke-width="3"/></svg></div>
</section>

<section class="row-one">
  <div class="abs feature panel-green">
    <h2>KORU APP</h2>
    <div class="abs phone-shot" role="img" aria-label="Smartphone showing the KORU app with room list, lamp toggles and colour swatches"></div>
    <div class="abs app-copy">
      <p>KORU Application allows you to control each lightbulb at home. Manage your lighting by creating functional groups and adding/excluding lightbulbs. Correctly matched lighting will help you work more productively and relax to the outmost.</p>
      <p>Create light scenes and adapt them to your needs. KORU App memorizes your favorite moods, so that you can use your settings anytime.</p>
      <p>Play with million colors and adjust the brightness of your home lighting. KORU works on NovaOS 3+ and Droidex 2+.</p>
    </div>
  </div>
  <div class="abs feature panel-dark">
    <h2 style="left:46px">KORU and Color</h2>
    <div class="abs color-shot" role="img" aria-label="Room lit by a green KORU lamp over houseplants with a tablet showing the app"></div>
    <div class="abs color-copy"><p>Experiment with millions of colors! Pick any color from the screen of your mobile device and enjoy the ambience. LED lightbulb KORU can transform conventional lighting into the night lights of Seattle or bring in the rich summer hues of Provence. Enliven your fantasies or raise your best memories in one click. Change the atmosphere around you by changing colors. You will literally see the world in a new light.</p></div>
  </div>
  <div class="abs scroll-cue" style="top:507px"><svg width="18" height="12" viewBox="0 0 18 12"><path d="M2 2l7 7 7-7" fill="none" stroke="#666" stroke-width="3"/></svg></div>
</section>

<section class="row-two">
  <div class="abs feature panel-darker">
    <h2>KORU and Health</h2>
    <div class="abs health-icon" role="img" aria-label="Illustration of a red heart with a heartbeat line"></div>
    <div class="abs health-copy">
      <p>Choose a scene for setting the alarm and improve your sleep naturally. KORU lighting system creates the necessary conditions for normalizing your circadian rhythms. Set your smart lightbulbs to turn on: now you can wake up "on the sunny side" despite gloomy weather. KORU lighting system will reduce your stress level.</p>
      <p>10 preset moods provide positive impact on your health. Designed to be what your mind and body need. We developed predefined modes in accordance with physiological and psychological aspects of human activities.</p>
    </div>
  </div>
  <div class="abs feature panel-blue">
    <h2 style="left:46px">Lighting Design</h2>
    <div class="abs lamp-icon" role="img" aria-label="Illustration of a white desk lamp"></div>
    <div class="abs lamp-copy">
      <p>Wireless lightbulbs with BlueLink and ZigMesh help you implement the concept of the smart home. KORU makes it affordable. Real lighting design at your place, couldn't have been simpler.</p>
      <p>Create optimal lighting for each functional area - set the perfect light for your kitchen, living room and nursery. Name individual lightbulbs or groups of them, set your color mood, pick a palette for each room. Stay informed of every smart lightbulb's condition, save your settings and load them anytime.</p>
      <p>With KORU lightbulbs your home lighting fits your lifestyle perfectly!</p>
    </div>
  </div>
  <div class="abs scroll-cue" style="top:506px"><svg width="18" height="12" viewBox="0 0 18 12"><path d="M2 2l7 7 7-7" fill="none" stroke="#666" stroke-width="3"/></svg></div>
</section>

<section class="specs">
  <h2>KORU Technical Specifications</h2>
  <div class="abs tools-icon" role="img" aria-label="Illustration of a crossed wrench and screwdriver"></div>
  <div class="abs spec-copy">
    <p>KORU lightbulb is a 85W incandescent equivalent that transforms your visual environment.</p>
    <p>E27 socket: no need to change anything. Easy way to home automation at hand. And yes, you can still use those switches.</p>
    <p>12.5W (110 - 230V,50Hz), 1000lm+: energy efficient LED lightbulb KORU shines brighter than others and saves energy.</p>
    <p>2700-5500K: You are not limited in your choice of color temperature. Turn on warm or cold light depending on your activities.</p>
  </div>
  <div class="abs compat">
    <h3>Compatibility:</h3>
    <ul>
      <li>Nova phone series 3 or newer</li>
      <li>Nova tablet, all models</li>
      <li>Nova player 2nd generation or newer</li>
      <li>All Droidex devices with BlueLink 2 or newer</li>
    </ul>
  </div>
</section>

<section class="signup">
  <div class="abs signup-photo" role="img" aria-label="Dim photograph of a KORU lightbulb on a dark wooden surface"></div>
  <h2>GET YOUR KORU</h2>
  <p>Cras vel dolor a ipsum eleifend auctor. Donec egestas ut diam ut iaculis. Nam id sem in quam gravida malesuada a lobortis risus</p>
  <div class="abs email-field">
    <svg width="16" height="12" viewBox="0 0 16 12"><rect x="0" y="0" width="16" height="12" fill="#444"/><path d="M0 0l8 7 8-7" fill="none" stroke="#fff" stroke-width="1.5"/></svg>
    <span>Email Address</span>
    <div class="email-go"><svg width="12" height="16" viewBox="0 0 12 16"><path d="M3 2l6 6-6 6" fill="none" stroke="#444" stroke-width="3"/></svg></div>
  </div>
</section>

<footer class="site-footer">
  <div class="abs footer-col contact-col">
    <h4>Contact info</h4>
    <div class="contact-item">
      <svg width="22" height="20" viewBox="0 0 22 20"><path d="M11 1 1 10h3v9h5v-6h4v6h5v-9h3z" fill="#ccc"/></svg>
      <span>Cras vel dolor ipsum<br>eleifend auctor.</span>
    </div>
    <div class="contact-item phone">
      <svg width="22" height="18" viewBox="0 0 22 18"><path d="M2 6c0-4 18-4 18 0v2h-5V6H7v2H2z" fill="#ccc"/><rect x="5" y="9" width="12" height="8" rx="2" fill="#ccc"/></svg>
      <span>555.010.2550</span>
    </div>
    <div class="contact-item">
      <svg width="22" height="16" viewBox="0 0 22 16"><rect width="22" height="16" rx="2" fill="#ccc"/><path d="M1 1l10 8 10-8" fill="none" stroke="#3a3a3a" stroke-width="2"/></svg>
      <span>info@koru-example.io</span>
    </div>
  </div>
  <div class="abs footer-col social-col">
    <h4>Stay in touch</h4>
    <div class="social-item"><span class="social-dot"></span>Like Us on Facenote</div>
    <div class="social-item"><span class="social-dot"></span>Watch Us on ViewTube</div>
    <div class="social-item"><span class="social-dot"></span>Follow Us on Chirper</div>
    <div class="social-item"><span class="social-dot"></span>Add Us on Circleplus</div>
  </div>
  <div class="abs legal-col">
    <div class="links">Home <span>|</span> Pre-order <span>|</span> Blog <span>|</span> Contact Us</div>
    <div>© 2014 koru-example.io. All rights reserved</div>
  </div>
</footer>

</body>
</html>
```